Professioal/Creative Northern Harbor Life Insurance Business Card Needed

I need a a creative and professional business card designed for Northern Harbor Life Insurance. Northern Harbor is a life insurance company that caters to mainly blue collar union workers life police, firefighters, teachers, truck drivers, steelworkers, etc. I would like a business card designed that is very professional. The final design should communicate professionalism and life security.

Must compliment company design and logo.

Here is the company website https://www.nhbrlife.example/#&panel1-1

Target Market(s)

Blue collar workers

Industry/Entity Type

Business

Contact Information for Business Card

Business card should have company logo and comply with colors. Here is the company website https://www.nhbrlife.example/#&panel1-1

Requirements
Must have
• Name: Dario Menke
• Producer

```html
<!DOCTYPE html>
<html lang="en">
<head>
<meta charset="utf-8">
<title>Northern Harbor Life Insurance — Business Card</title>
<link rel="stylesheet" href="https://fonts.googleapis.com/css2?family=Marcellus+SC&family=Open+Sans:wght@400&display=swap">
<style>
  :root {
    --page-bg: #d9d2ca;
    --card-bg: #efeae4;
    --card-edge: #e2dbd3;
    --divider: #d6cdc3;
    --ink: #4a4440;
    --ink-soft: #6e6660;
    --brand-brown: #6b2a12;
    --brand-brown-deep: #4e1a0a;
    --brand-orange: #c46a22;
    --brand-orange-light: #e09a52;
    --url-ink: #e8cfb8;
  }
  html, body {
    margin: 0;
    width: 1200px;
    height: 1200px;
    overflow: hidden;
    background: var(--page-bg);
  }
  .card {
    position: absolute;
    left: 100px;
    top: 303px;
    width: 1000px;
    height: 594px;
    background: var(--card-bg);
    border: 1px solid var(--card-edge);
    box-sizing: border-box;
    overflow: hidden;
    font-family: "Open Sans", sans-serif;
  }
  .card__divider {
    position: absolute;
    left: 505px;
    top: 0;
    width: 1px;
    height: 516px;
    background: var(--divider);
  }
  .brand {
    position: absolute;
    left: 0;
    top: 0;
    width: 505px;
    height: 516px;
    display: flex;
    align-items: center;
    justify-content: center;
    gap: 18px;
  }
  .brand__dot {
    width: 64px;
    height: 64px;
    border-radius: 50%;
    background: var(--brand-brown);
    flex: none;
  }
  .brand__name {
    font-family: "Open Sans", sans-serif;
    font-size: 30px;
    font-weight: 400;
    color: var(--brand-brown);
    line-height: 1.15;
  }
  .person {
    position: absolute;
    left: 583px;
    top: 160px;
  }
  .person__name {
    font-family: "Marcellus SC", serif;
    font-size: 38px;
    color: var(--ink);
    margin: 0;
    line-height: 1;
    letter-spacing: 0.5px;
  }
  .person__title {
    font-size: 22px;
    color: var(--ink-soft);
    margin: 18px 0 0;
  }
  .contacts {
    position: absolute;
    left: 592px;
    top: 280px;
    margin: 0;
    padding: 0;
    list-style: none;
  }
  .contacts__item {
    display: flex;
    align-items: center;
    height: 37px;
    font-size: 23px;
    color: var(--ink);
  }
  .contacts__icon {
    width: 24px;
    height: 24px;
    margin-right: 22px;
    flex: none;
  }
  .band {
    position: absolute;
    left: 0;
    bottom: 0;
    width: 1000px;
    height: 78px;
  }
  .band__url {
    position: absolute;
    left: 583px;
    bottom: 24px;
    font-size: 22px;
    color: var(--url-ink);
    letter-spacing: 0.3px;
  }
</style>
</head>
<body>
  <div class="card">
    <div class="brand">
      <span class="brand__dot"></span>
      <span class="brand__name">Northern Harbor</span>
    </div>

    <div class="card__divider"></div>

    <div class="person">
      <h1 class="person__name">Dario Menke</h1>
      <p class="person__title">Producer</p>
    </div>

    <ul class="contacts">
      <li class="contacts__item">
        <svg class="contacts__icon" viewBox="0 0 24 24" aria-hidden="true">
          <path d="M3 9c0-3 4-5 9-5s9 2 9 5v2h-5V9H8v2H3z" fill="var(--brand-orange)"/>
          <path d="M6 12h12l2 8H4z" fill="var(--brand-orange)"/>
          <circle cx="12" cy="16" r="2.4" fill="var(--card-bg)"/>
        </svg>
        1-800-555-0142
      </li>
      <li class="contacts__item">
        <svg class="contacts__icon" viewBox="0 0 24 24" aria-hidden="true">
          <rect x="7" y="3" width="10" height="6" fill="var(--brand-orange)"/>
          <rect x="3" y="9" width="18" height="8" rx="1.5" fill="var(--brand-orange)"/>
          <rect x="7" y="14" width="10" height="7" fill="var(--brand-orange)" stroke="var(--card-bg)" stroke-width="1.5"/>
        </svg>
        (254) 555-0187
      </li>
      <li class="contacts__item">
        <svg class="contacts__icon" viewBox="0 0 24 24" aria-hidden="true">
          <rect x="2" y="6" width="20" height="13" fill="var(--brand-orange)"/>
          <path d="M2 6l10 8 10-8" fill="none" stroke="var(--card-bg)" stroke-width="1.6"/>
        </svg>
        dariomenke@nhbrlife.example
      </li>
    </ul>

    <svg class="band" viewBox="0 0 1000 78" preserveAspectRatio="none" aria-hidden="true">
      <defs>
        <linearGradient id="band-orange" x1="0" y1="0" x2="0" y2="1">
          <stop offset="0" stop-color="var(--brand-orange-light)"/>
          <stop offset="1" stop-color="var(--brand-orange)"/>
        </linearGradient>
        <linearGradient id="band-brown" x1="0" y1="0" x2="1" y2="0">
          <stop offset="0" stop-color="var(--brand-brown)"/>
          <stop offset="1" stop-color="var(--brand-brown-deep)"/>
        </linearGradient>
      </defs>
      <rect x="0" y="38" width="520" height="40" fill="url(#band-orange)"/>
      <polygon points="528,0 1000,0 1000,78 487,78" fill="url(#band-brown)"/>
    </svg>
    <span class="band__url">www.nhbrlife.example</span>
  </div>
</body>
</html>
```